Produktdesign - Kosmetikprodukt
Zielgruppe
Damen ab 50
Aufgabenstellung
Ausgeschrieben wird ein ansprechendes und hochwertiges Produktdesign für eine neu einzuführende Creme zur Vergrößerung der weiblichen Brust.
Produktname: soleva amarin
Verpackung: Weiße Tube mit Schraubverschluss
Zu verwendende Begriffe auf der Vorderseite:
- soleva amarin als edler Schriftzug
- VOLUME effect
- DETOX effect
- FIRMING effect
Zu verwendende Informationen auf der Rückseite:
Mit Dreifach-Wirkkomplex....
VOLUME effect: stimuliert die Adipozytendifferenzierung, damit
funktionsfähige Adipozyten entstehen - positiver Effekt auf Volumen
DETOX effect: Tessalin aktiviert Proteasome 20S, die beschädigte
Zellen beseitigt und so die Zelltoxizität herabsetzt.
FIRMING effect: steigert die Dynamik der Fibrolasten um die Matrix
Wechselwirkungen wiederherzustellen.
- Barcode mit EAN: 4019283746512
- Inhalt: 50ml
- Made in germany
- Kelbrand GmbH, Anton - Feiler - Str. 7, 34567 Musterdorf

```html
<!DOCTYPE html>
<html lang="de">
<head>
<meta charset="utf-8">
<title>soleva amarin – Tube</title>
<link rel="stylesheet" href="https://fonts.googleapis.com/css2?family=Josefin+Sans:wght@400&family=Share+Tech+Mono&display=swap">
<style>
  :root {
    --paper: #ffffff;
    --ink: #1a1a1a;
    --teal: #009bb0;
    --outline: #2b2b2b;
    --shade: #9a9a9c;
    --shade-soft: #d9d9db;
    --silver-dark: #8e8e90;
    --silver-light: #f4f4f5;
  }
  html, body {
    margin: 0;
    padding: 0;
    width: 1200px;
    height: 3642px;
    overflow: hidden;
    background: var(--paper);
  }
  .tube {
    display: block;
    width: 1200px;
    height: 3642px;
  }
  .brand-line {
    font-family: "Josefin Sans", sans-serif;
    font-variant: small-caps;
    font-size: 64px;
    letter-spacing: 9px;
    fill: var(--ink);
  }
  .claim {
    font-family: "Share Tech Mono", monospace;
    font-size: 37px;
    letter-spacing: 5px;
    fill: var(--teal);
  }
  .rule { stroke: var(--teal); stroke-width: 2.5; }
  .brand-square { fill: var(--teal); }
  .edge { fill: none; stroke: var(--outline); stroke-width: 1.2; }
  .tick { stroke: #bdbdbf; stroke-width: 1.5; }
</style>
</head>
<body>
<svg class="tube" viewBox="0 0 670 2034" preserveAspectRatio="none" xmlns="http://www.w3.org/2000/svg">
  <defs>
    <linearGradient id="body-shade" x1="0" x2="1" y1="0" y2="0">
      <stop offset="0" stop-color="var(--shade)"/>
      <stop offset="0.12" stop-color="var(--shade-soft)"/>
      <stop offset="0.3" stop-color="var(--paper)"/>
      <stop offset="0.75" stop-color="var(--paper)"/>
      <stop offset="0.9" stop-color="var(--shade-soft)"/>
      <stop offset="1" stop-color="var(--shade)"/>
    </linearGradient>
    <linearGradient id="cap-shade" x1="0" x2="1" y1="0" y2="0">
      <stop offset="0" stop-color="var(--silver-dark)"/>
      <stop offset="0.25" stop-color="#c8c8ca"/>
      <stop offset="0.55" stop-color="var(--silver-light)"/>
      <stop offset="0.8" stop-color="#c4c4c6"/>
      <stop offset="1" stop-color="var(--silver-dark)"/>
    </linearGradient>
  </defs>

  <!-- crimped seal -->
  <g class="seal">
    <rect x="33" y="8" width="605" height="66" fill="var(--paper)" class="edge"/>
    <g>
      <line class="tick" x1="60" y1="18" x2="60" y2="48"/>
      <line class="tick" x1="105" y1="18" x2="105" y2="48"/>
      <line class="tick" x1="150" y1="18" x2="150" y2="48"/>
      <line class="tick" x1="195" y1="18" x2="195" y2="48"/>
      <line class="tick" x1="240" y1="18" x2="240" y2="48"/>
      <line class="tick" x1="285" y1="18" x2="285" y2="48"/>
      <line class="tick" x1="330" y1="18" x2="330" y2="48"/>
      <line class="tick" x1="375" y1="18" x2="375" y2="48"/>
      <line class="tick" x1="420" y1="18" x2="420" y2="48"/>
      <line class="tick" x1="465" y1="18" x2="465" y2="48"/>
      <line class="tick" x1="510" y1="18" x2="510" y2="48"/>
      <line class="tick" x1="555" y1="18" x2="555" y2="48"/>
      <line class="tick" x1="600" y1="18" x2="600" y2="48"/>
    </g>
    <rect x="33" y="72" width="605" height="12" fill="#a7a7a9"/>
  </g>

  <!-- tube body -->
  <path class="tube-body" fill="url(#body-shade)" d="M35 84 L636 84 C620 420 560 760 545 1050 L540 1700 L150 1700 L140 1050 C120 760 50 420 35 84 Z"/>
  <path class="edge" d="M35 84 C50 420 120 760 140 1050 L150 1700 M636 84 C620 420 560 760 545 1050 L540 1700"/>

  <!-- screw cap -->
  <path class="cap" fill="url(#cap-shade)" d="M150 1695 C240 1712 450 1712 540 1695 L540 2018 C450 2030 240 2030 150 2018 Z"/>
  <path class="edge" d="M150 1695 C240 1712 450 1712 540 1695 L540 2018 C450 2030 240 2030 150 2018 Z"/>

  <!-- brand name -->
  <text class="brand-line" x="335" y="470" text-anchor="middle">Soleva</text>
  <line class="rule" x1="165" y1="493" x2="503" y2="493"/>
  <text class="brand-line" x="335" y="557" text-anchor="middle">Amarin</text>
  <rect class="brand-square" x="283" y="608" width="104" height="104" rx="12"/>

  <!-- claims -->
  <g class="claims">
    <text class="claim" x="335" y="810" text-anchor="middle">VOLUME</text>
    <text class="claim" x="335" y="860" text-anchor="middle">EFFECT</text>
    <text class="claim" x="335" y="960" text-anchor="middle">DETOX</text>
    <text class="claim" x="335" y="1011" text-anchor="middle">EFFECT</text>
    <text class="claim" x="335" y="1112" text-anchor="middle">FIRMING</text>
    <text class="claim" x="335" y="1163" text-anchor="middle">EFFECT</text>
  </g>
</svg>
</body>
</html>
```